Wine Bottle Label for Tall Fern Cellars

We are a small, newly established winery in need of an original, bold and outstanding bottle label design for our Tall Fern wine.

Our vineyard and winery are located on a 200 acre farm in a remote part of southern Oregon. The name "Tall Fern" was inspired by the large, overgrown size of all of the foliage here, including our grapevines. Things grow large and vigorous in Oregon! And everything is very lush and green. It is almost surreal or other-worldly, like the landscapes seen in the Keeper of The Hollows movies, or the land of Yarrowmere. It is a place that makes you say "wow" with its epic, large scale, natural beauty.

The name "Tall Fern" also captures the essence of our wine. It is big in flavor, quality and color. Our first release is a Pinot Noir (red). Pinot Noir wines often are subtle in flavor and thin in their color. Our label should convey that our Pinot Noir is a much more robust, darker, heavier, meatier, more flavorful wine that is a lot more fun than an "ordinary" wine. At the same time, this wine is not cheap, and so nothing in the label should convey "bargain," "low price," or "cheapness." This is a fine wine with a sense of adventure. Be sure to convey "quality" with your design along with "big," "adventure" and "fun".

The label should appeal to a younger demographic, both male and female, between the ages of 21 and 35. It should be non-traditional and adventurous and suggest a pushing of boundaries and a breaking of rules. This Pinot Noir does not conform to the normal "limitations" of the variety, therefore the label should not conform. It should have an "organic" or "natural" or "agricultural" vibe, as opposed to something mechanical or technical. It should, however, be contemporary. Do not confuse "natural" or "organic" with being nostalgic or old school. Think "agri-hipsters."

The label should be designed to fit on a Burgundy-style wine bottle (photo attached for reference). (Note: All Pinot Noir and Chardonnay is bottled in Burgundy bottles, If you are not sure about the bottle shape you can go to a local store and compare the various bottles. Locate a bottle of Pinot Noir or Chardonnay or anything identified as a "Burgundy Wine," and it should be the correct bottle. The tall, skinny bottles used for Cabernet Sauvignon are NOT correct)). Please see the "Must Have" notes for more on the bottle.

In summary, the final project should be a wine bottle label design that conveys bigness, vastness, adventurous, non-traditional, high quality wine. A good tagline to keep in mind is "Living Large."

Target Market(s)

Young, hip, non-conformist wine drinkers aged 21-35 with a sense of adventure and an appreciation of quality.

Industry/Entity Type

School

Requirements
Must have
• *Must contain the words:

Tall Fern (the brand)
2013 Pinot Noir (the vintage year and variety)

*The label must be designed to fit a Burgundy-style wine bottle. A photo is attached for reference.

*Additionally, the label needs to fit on the lower, widest part of the bottle. The label will be printed on sticky paper and rolled onto the bottle with a machine. The machine cannot apply labels to the neck of the bottle. The maximum size of a label that will fit this space is 5.5 inches wide by 4.5 inches tall. You DO NOT have to fill ALL of this space or confine the label shape to a rectangle, but the label cannot exceed this size or it won't stick to the bottle properly. It will really help if you can put your hands on an actual bottle to see the logistics of applying the label. But if that is not possible, just do your best with the instructions you have. I am confident the winning design could be adjusted to fit the bottle, if necessary
Nice to have
• *Wine grape leaf or leaves.

*A concept I have been playing with is sunlight shining through leaves like light through a Kessler lamp or a stained glass window. This is NOT a requirement for this label. However, if the concept inspires and idea, I would be most happy to see it.
Should not have
• IF a leaf or leaves are included in the design (not a requirement) they MUST be wine grapevine leafs and preferably leaves of the Pinot Noir vine. Do not use generic leaves or identifiable leaves such as oak leaves, maple leaves, or anything that looks like the Canadian flag or the Dunmore Ice Hawks hockey logo. Reference the attached photos of wine grape leaves to see the correct leaf type. I am happy to email more photos upon request. These photos may be used in whole or in part in your design, however, a leaf from a photo is NOT a requirement, nor is the image of a leaf or leaves.

This label should NOT be designed for Bordeaux-style wine bottles (the tall, skinny ones).

```html
<!DOCTYPE html>
<html lang="en">
<head>
<meta charset="utf-8">
<title>Tall Fern Cellars – 2013 Pinot Noir Label</title>
<link rel="stylesheet" href="https://fonts.googleapis.com/css2?family=Oswald:wght@300;400;500&display=swap">
<style>
  :root {
    --page: #ffffff;
    --label-black: #000000;
    --wine-red: #8b1303;
    --wine-red-deep: #6e0e02;
    --bottle-green: #8f9a2c;
    --bottle-dark: #3c4410;
  }
  html, body {
    margin: 0;
    padding: 0;
    width: 1200px;
    height: 997px;
    overflow: hidden;
    background: var(--page);
  }
  .canvas {
    position: relative;
    width: 1200px;
    height: 997px;
  }
  .label-art {
    position: absolute;
    left: 0;
    top: 0;
    width: 1200px;
    height: 997px;
  }
  .label-type {
    font-family: "Oswald", sans-serif;
    fill: var(--wine-red);
  }
  .label-type--place {
    font-weight: 500;
    font-size: 31px;
    letter-spacing: 4px;
  }
  .label-type--year {
    font-weight: 500;
    font-size: 38px;
    letter-spacing: 2px;
  }
  .label-type--brand {
    font-weight: 400;
    font-size: 80px;
    fill: var(--label-black);
    stroke: var(--wine-red);
    stroke-width: 2.4px;
  }
  .label-type--variety {
    font-weight: 400;
    font-size: 29px;
    letter-spacing: 5px;
    fill: var(--label-black);
  }
  .label-type--legal {
    font-weight: 300;
    font-size: 22px;
    letter-spacing: -0.5px;
  }
</style>
</head>
<body>
<main class="canvas">
  <svg class="label-art" viewBox="0 0 1200 997" xmlns="http://www.w3.org/2000/svg">
    <defs>
      <radialGradient id="leaf-tone" cx="50%" cy="45%" r="60%">
        <stop offset="0%" stop-color="var(--wine-red)"/>
        <stop offset="100%" stop-color="var(--wine-red-deep)"/>
      </radialGradient>
      <linearGradient id="bottle-tone" x1="0" x2="1" y1="0" y2="0">
        <stop offset="0%" stop-color="var(--bottle-dark)"/>
        <stop offset="45%" stop-color="var(--bottle-green)"/>
        <stop offset="100%" stop-color="var(--bottle-dark)"/>
      </linearGradient>
    </defs>

    <path class="label-body" fill="var(--label-black)"
      d="M128 167 H847 A35 35 0 0 0 882 202 V778 A35 35 0 0 0 847 813 H128 A35 35 0 0 0 93 778 V202 A35 35 0 0 0 128 167 Z"/>

    <path class="label-frame" fill="none" stroke="var(--wine-red)" stroke-width="2"
      d="M134 178 H841 A37 37 0 0 0 871 208 V772 A37 37 0 0 0 841 802 H134 A37 37 0 0 0 104 772 V208 A37 37 0 0 0 134 178 Z"/>

    <ellipse class="leaf-art" role="img" aria-label="Large red grapevine leaf silhouette with a long stem"
      cx="488" cy="480" rx="240" ry="275" fill="url(#leaf-tone)"/>

    <rect class="title-band" x="209" y="420" width="557" height="90" fill="var(--label-black)"/>
    <rect class="title-rule" x="209" y="416" width="557" height="3" fill="var(--wine-red)"/>
    <rect class="title-rule" x="209" y="509" width="557" height="3" fill="var(--wine-red)"/>

    <text class="label-type label-type--place" x="149" y="248">ROSEVILLE</text>
    <text class="label-type label-type--place" x="829" y="248" text-anchor="end">OREGON</text>

    <text class="label-type label-type--year" x="218" y="482">20</text>
    <text class="label-type label-type--year" x="759" y="482" text-anchor="end">13</text>

    <text class="label-type label-type--brand" x="310" y="495" textLength="356" lengthAdjust="spacingAndGlyphs">TALL FERN</text>

    <text class="label-type label-type--variety" x="488" y="555" text-anchor="middle">-PINOT NOIR-</text>

    <text class="label-type label-type--legal" x="149" y="756">ALC. 12.5% BY VOL.</text>
    <text class="label-type label-type--legal" x="826" y="756" text-anchor="end">750 ML ℮</text>

    <path class="bottle-preview" role="img" aria-label="Burgundy-style wine bottle wearing the Tall Fern label"
      fill="url(#bottle-tone)"
      d="M1017 293 H1046 V330 C1048 420 1090 450 1090 520 V690 Q1090 700 1080 700 H978 Q968 700 968 690 V520 C968 450 1015 420 1017 330 Z"/>
  </svg>
</main>
</body>
</html>
```